Label Design for RTD Cocktail Line Tovelin Spirits

Tovelin Spirits is a line of Indian-inspired artisan cocktails that "brings the bartender home" for professional men and women who like the finer things in life but don’t always have the time to treat themselves. No need for a multitude of expensive and hard-to-find ingredients, time consuming recipes, or a mixologist.

Our line of 3 open and serve cocktails blends a range of premium spirits with exotic ingredients so you can conveniently raise a glass for any of life’s celebrations.

Our bottle is the 750ml Claret bottle with Quarnet (screw cap) closure and will be covered entirely in a shrink sleeve (so potentially anything can be designed for any part of the bottle). We want the bottle to pop on the shelf so it should look different than what’s already out there (Velvet Moth, Galdrova, Merlusa ready to drink cocktails). We are looking for a sexy design that's polished/sleek.
Updates

Project Deadline Extended
Reason: Hello designers! Tovelin Spirits is so impressed with what we have received thus far and we would like to give some of the designers a few extra days to make the edits we requested. It's never too late to submit! Thank you all!

Industry/Entity Type

It Professional

Requirements
Must have
• Front of bottle
* “Tovelin Spirits” name and Peacock Logo- but feel free to pull the elements apart and use them on the bottle in different ways
* Open & Serve
* 12% ALC/VOL
* 750 ml
* 3 different labels in a theme for
-Borvelle
-Faluntera
-Pomadrine

Borvelle Ideas- soft brown palate, the ingredients in chai spice (cloves, cardamom pods, nutmeg, black peppercorns, star anise, and cinnamon stick)

Faluntera Ideas -cool and refreshing, pale green shade (not clashing with logo), graphics of fresh mint leaves, green chili, lime, cucumber

Pomadrine Ideas- soft/pale pink shades, graphics of lychi fruit (outer red shell and inner pink flesh), ginger

Back of bottle
* explanation of the 3 cocktails
Borvelle: Forget what you think you know about chai, this is not the Queen’s tea-time drink! Borvelle is a smooth, sweetly -spiced cocktail made with vodka, black tea, and a combination of aromatic spices. This velvety cocktail is rich without being heavy. Enjoy chilled or over ice anytime.

Faluntera: Faluntera can’t make up its mind! This fusion of zesty lime, sweet mint, earthy cucumber and spicy chilies is so refreshing you’ll crave it on a hot summer day or a cool winter’s night. The exotic botanicals in gin add a complexity to the cocktail making this a refreshing but potent drink! Enjoy chilled or over ice anytime.

Pomadrine: East meet West. Delicate lychi meet hard-hitting whiskey. Pomadrine will tempt you senses with flavor, fragrance and beauty. The peppery kick of ginger and the intensity of the un-aged whiskey are softened by lychi’s intoxicating scent and subtle, sweet finish.

Please include
1. Bottled By QRW Spirits Company
2. Sample barcode (where you would place it in your design)
3. www.TovelinSpirits.example
4. GOVERNMENT WARNING: (1) According to the Surgeon General, women should not drink alcoholic beverages during pregnancy because of the risk of birth defects. (2) Consumption of alcoholic beverages impairs your ability to drive a car or operate machinery, and may cause health problems.

Optional to include
*"Bring the Bartender Home"
*"Tovelin Spirits” name and Peacock Logo on the back
*Entirely black sleeve with contrasting design

FYI the Fonts used in our logo are Geosans Light and Prakrta, but feel free to use other complimentary fonts on the other aspects.
Nice to have
• Optional to include

```html
<!DOCTYPE html>
<html lang="en">
<head>
<meta charset="utf-8">
<title>Tovelin Spirits – Borvelle Cocktails Sleeve</title>
<link rel="stylesheet" href="https://fonts.googleapis.com/css2?family=Oswald:wght@600&family=Arimo:wght@400;700&display=swap">
<style>
  :root {
    --backdrop: #000000;
    --sleeve-core: #f9a23a;
    --sleeve-mid: #ef6e1c;
    --sleeve-edge: #c9261a;
    --label-white: #ffffff;
    --title-red: #e3261f;
    --brand-blue: #1d5f9c;
    --brand-dot: #2bb673;
    --ink: #2b2b2b;
    --accent-orange: #f28a1e;
    --tea-dark: #2a221c;
    --tea-warm: #5a3a24;
    --splash-orange: #f6a436;
  }

  html, body {
    margin: 0;
    padding: 0;
    width: 1200px;
    height: 2180px;
    overflow: hidden;
    background: var(--backdrop);
  }

  .stage {
    position: relative;
    width: 1200px;
    height: 2180px;
    overflow: hidden;
    background: var(--backdrop);
    font-family: "Arimo", Arial, sans-serif;
  }

  .bottle-sleeve {
    position: absolute;
    left: 0;
    top: 0;
    width: 1200px;
    height: 2180px;
  }

  .front-label {
    position: absolute;
    left: 400px;
    top: 950px;
    width: 400px;
    height: 1010px;
    background: var(--label-white);
    border-radius: 40px;
    text-align: center;
    color: var(--ink);
  }

  .brand {
    position: absolute;
    top: 24px;
    left: 0;
    width: 100%;
    display: flex;
    flex-direction: column;
    align-items: center;
  }

  .brand-dot {
    width: 76px;
    height: 76px;
    border-radius: 50%;
    background: var(--brand-dot);
    margin-bottom: 18px;
  }

  .brand-name {
    font-weight: 700;
    font-size: 32px;
    line-height: 1;
    color: var(--brand-blue);
  }

  .product-name {
    position: absolute;
    top: 196px;
    left: 0;
    width: 100%;
    margin: 0;
    font-family: "Oswald", "Arial Narrow", sans-serif;
    font-weight: 600;
    font-size: 96px;
    line-height: 1;
    letter-spacing: 1px;
    color: var(--title-red);
  }

  .product-line {
    position: absolute;
    top: 306px;
    left: 0;
    width: 100%;
    font-size: 38px;
    line-height: 1;
    color: var(--ink);
  }

  .serve-note {
    position: absolute;
    top: 876px;
    left: 0;
    width: 100%;
    font-size: 30px;
    line-height: 1.2;
    color: var(--ink);
  }

  .serve-note .volume {
    display: block;
    font-weight: 700;
    color: var(--accent-orange);
  }

  .strength {
    position: absolute;
    top: 970px;
    left: 0;
    width: 100%;
    font-size: 18px;
    color: var(--ink);
  }

  .ingredient-art {
    position: absolute;
    left: 320px;
    top: 1310px;
    width: 540px;
    height: 500px;
    overflow: visible;
  }
</style>
</head>
<body>
  <main class="stage">
    <svg class="bottle-sleeve" viewBox="0 0 1200 2180">
      <defs>
        <linearGradient id="sleeve-tone" x1="0" y1="0" x2="1" y2="0">
          <stop offset="0" stop-color="var(--sleeve-edge)"/>
          <stop offset="0.25" stop-color="var(--sleeve-mid)"/>
          <stop offset="0.5" stop-color="var(--sleeve-core)"/>
          <stop offset="0.75" stop-color="var(--sleeve-mid)"/>
          <stop offset="1" stop-color="var(--sleeve-edge)"/>
        </linearGradient>
        <radialGradient id="swash-tone" cx="0.5" cy="0.35" r="0.6">
          <stop offset="0" stop-color="#ffd08a" stop-opacity="0.45"/>
          <stop offset="1" stop-color="#b81e14" stop-opacity="0.2"/>
        </radialGradient>
        <clipPath id="bottle-shape">
          <path d="M488 56 Q488 40 504 40 L680 40 Q696 40 696 56 L696 120 L690 130 L690 300
                   C690 480 880 560 880 760 L880 2060 Q880 2100 840 2100 L360 2100
                   Q320 2100 320 2060 L320 760 C320 560 500 480 500 300 L500 130 L488 120 Z"/>
        </clipPath>
      </defs>
      <g clip-path="url(#bottle-shape)">
        <rect x="300" y="30" width="600" height="2080" fill="url(#sleeve-tone)"/>
        <rect x="300" y="30" width="600" height="2080" fill="url(#swash-tone)"
              role="img" aria-label="Loose red and orange brush strokes across the sleeve"/>
      </g>
    </svg>

    <section class="front-label">
      <div class="brand">
        <span class="brand-dot"></span>
        <span class="brand-name">Tovelin Spirits</span>
      </div>

      <h1 class="product-name">BORVELLE</h1>
      <div class="product-line">COCKTAILS</div>

      <div class="serve-note">
        OPEN &amp; SERVE
        <span class="volume">750ml</span>
      </div>
      <div class="strength">12% ALC/VOL</div>
    </section>

    <svg class="ingredient-art" viewBox="0 0 540 500" role="img" aria-label="Orange paint swirl with bubbles around loose black chai tea leaves, with star anise at the right">
      <defs>
        <radialGradient id="splash-tone" cx="0.5" cy="0.5" r="0.5">
          <stop offset="0" stop-color="var(--tea-dark)"/>
          <stop offset="0.42" stop-color="var(--tea-warm)"/>
          <stop offset="0.55" stop-color="var(--splash-orange)"/>
          <stop offset="0.85" stop-color="var(--splash-orange)" stop-opacity="0.5"/>
          <stop offset="1" stop-color="var(--splash-orange)" stop-opacity="0"/>
        </radialGradient>
      </defs>
      <ellipse cx="270" cy="250" rx="265" ry="245" fill="url(#splash-tone)"/>
    </svg>
  </main>
</body>
</html>
```